Refresh web site from year 2003

Voltaro Works has a web site (https://vowrk-site.no/) from early 2000 that needs to be refreshed.

Attached are company logo, favicon files, a licensed image to be used, an animation that illustrate the use of one of the products.

Target Market(s)

Industrial customers

Industry/Entity Type

Electrical Switch Board Builders, Automation Industry

Coding

Coded - Design and coding required

Number of Pages Required

3 page

Requirements
Must have
• WordPress site. Use attached animation in the front page (source file is in Adobe Animation format, if adjustments are needed). Product page for two products, "KTR" and "QX-7 Ver B".
Nice to have
• The site should focus on promoting two products KTR and QX-7 Ver B.

```html
<!DOCTYPE html>
<html lang="en">
<head>
<meta charset="utf-8">
<title>Voltaro Works</title>
<link href="https://fonts.googleapis.com/css2?family=Poppins:wght@300;400;500;600&display=swap" rel="stylesheet">
<style>
:root{
  --blue:#0a4b8c;
  --blue-dark:#083f77;
  --ink:#222;
  --muted:#555;
  --line:#e2e2e2;
  --card:#f3f3f3;
  --white:#fff;
}
*{box-sizing:border-box;margin:0;padding:0}
html,body{width:1200px;height:3372px;overflow:hidden}
body{position:relative;font-family:'Poppins',sans-serif;color:var(--ink);background:var(--white)}
.abs{position:absolute}
a{color:inherit;text-decoration:none}

/* header */
.brand{font-weight:600;color:var(--blue);font-size:27px;line-height:1.1;letter-spacing:.3px}
.top-contact{display:flex;align-items:center;gap:10px;font-size:12.5px;line-height:1.25}
.top-contact .ico{width:30px;height:30px;border-radius:50%;background:var(--blue);display:flex;align-items:center;justify-content:center}
.top-contact .lbl{color:var(--blue)}
.lang{display:flex;align-items:center;gap:6px;font-size:12px}
.lang .dot{width:24px;height:24px;border-radius:50%;background:#c8102e}
.nav{display:flex;font-size:13px}
.nav a{position:absolute;white-space:nowrap}
.nav .active{color:var(--blue);font-weight:500}
.nav .active::after{content:"";position:absolute;left:0;right:-4px;top:33px;height:2px;background:var(--blue)}

/* hero */
.hero{left:0;top:122px;width:1200px;height:657px;background:linear-gradient(100deg,#d9dcdf 0%,#e8eaec 35%,#dfe2e4 60%,#b9c3cf 80%,#7d9dc9 100%)}
.hero-eyebrow{color:var(--blue);font-size:18px}
.hero-title{color:var(--blue);font-size:41px;font-weight:600;line-height:1}
.hero-desc{font-size:14px;line-height:16px;color:#333;width:300px}
.btn{display:flex;align-items:center;justify-content:space-between;background:var(--blue);color:var(--white);font-size:12.5px;padding:0 10px 0 26px}
.btn .arr{width:18px;height:18px;border-radius:50%;background:var(--white);display:flex;align-items:center;justify-content:center}
.btn.center{justify-content:center;padding:0}

/* section headings */
.h2{width:1200px;left:0;text-align:center;font-size:31px;font-weight:500;color:#222}
.h2.light{color:var(--white)}
.rule{width:58px;height:2px;background:var(--blue)}

/* about */
.about-frame{background:var(--blue);border-radius:14px 0 0 0}
.about-outline{border:2px solid var(--blue);border-radius:0 0 10px 0}
.about-photo{border-radius:14px;background:linear-gradient(90deg,#d6d8d6 0%,#eceeec 40%,#c9ccc8 60%,#e8e6df 100%)}
.about-text{font-size:13.8px;line-height:26.2px;color:var(--muted);font-weight:300;width:480px;white-space:nowrap}
.about-text p{margin-bottom:26.2px}
.about-text p:last-child{margin-bottom:0}
.about-text b{font-weight:600;color:#333}

/* services */
.services{left:0;top:1440px;width:1200px;height:603px;background:var(--blue)}
.svc{background:var(--white);border-radius:8px;overflow:hidden;width:335px;height:410px;top:1544px;text-align:center}
.svc .ph{height:250px}
.svc h3{font-weight:400;font-size:25px;margin-top:24px;color:#222}
.svc p{font-size:14.5px;line-height:17px;color:#333;margin:12px auto 0;width:260px}

/* products */
.prod{top:2176px;width:246px;height:280px;background:var(--card);border-radius:10px}
.prod .shape{position:absolute}
.prod-name{top:2476px;width:246px;text-align:center;font-size:24px;line-height:28px;letter-spacing:.5px;color:#222}

/* contact */
.contact-card{left:191px;top:2692px;width:813px;height:340px;background:var(--white);box-shadow:0 0 14px rgba(0,0,0,.08)}
.contact-card h2{text-align:center;font-weight:500;font-size:28px;margin-top:35px}
.field{border:1px solid var(--line);font-size:12.5px;color:#888;padding:12px 14px;background:var(--white)}

/* footer */
.footer{left:0;top:2896px;width:1200px;height:421px;background:var(--blue)}
.f-head{color:var(--white);font-size:13px;letter-spacing:.3px}
.f-head::after{content:"";display:block;width:38px;height:1.5px;background:var(--white);margin-top:9px}
.f-list{color:var(--white);font-size:13px;list-style:none}
.f-list li{position:absolute;white-space:nowrap}
.chev{display:inline-block;width:16px;font-size:11px}
.news-input{background:var(--white);border:1px solid #cfd8e3;font-size:13px;padding:0 15px;display:flex;align-items:center;color:#333}
.news-btn{background:var(--white);font-size:12.5px;display:flex;align-items:center;justify-content:center;color:#222;letter-spacing:.3px}
.copy{font-size:12.5px;color:#333}
.social{width:25px;height:25px;border-radius:50%;background:var(--blue-dark)}
.social.first{background:#1f6fd1}
</style>
</head>
<body>

<!-- header -->
<div class="abs brand" style="left:68px;top:48px">Voltaro Works</div>

<div class="abs top-contact" style="left:689px;top:26px">
  <div class="ico"><svg width="14" height="14" viewBox="0 0 24 24"><path fill="#fff" d="M6.6 10.8a15 15 0 0 0 6.6 6.6l2.2-2.2c.3-.3.7-.4 1-.2 1.1.4 2.3.6 3.6.6.6 0 1 .4 1 1V20c0 .6-.4 1-1 1A17 17 0 0 1 3 4c0-.6.4-1 1-1h3.5c.6 0 1 .4 1 1 0 1.3.2 2.5.6 3.6.1.3 0 .7-.2 1z"/></svg></div>
  <div><div class="lbl">Call Us</div><div>555-010-2040</div></div>
</div>
<div class="abs top-contact" style="left:846px;top:26px">
  <div class="ico"><svg width="14" height="11" viewBox="0 0 20 14"><rect x="1" y="1" width="18" height="12" rx="1.5" fill="none" stroke="#fff" stroke-width="1.6"/><path d="M1.5 1.5 10 8l8.5-6.5" fill="none" stroke="#fff" stroke-width="1.6"/></svg></div>
  <div><div class="lbl">Email us</div><div>info@voltaroworks.com</div></div>
</div>
<div class="abs lang" style="left:1060px;top:30px"><span class="dot"></span>ENG <span style="font-size:9px">&#8964;</span></div>

<nav class="nav abs" style="left:0;top:76px">
  <a class="active" href="#" style="left:666px">Home</a>
  <a href="#" style="left:746px">About us</a>
  <a href="#" style="left:843px">Our Services</a>
  <a href="#" style="left:962px">Products</a>
  <a href="#" style="left:1056px">Contact us</a>
</nav>

<!-- hero -->
<div class="abs hero" role="img" aria-label="Photo of an electrical switch cabinet with control buttons and a technician writing on a clipboard"></div>
<div class="abs hero-eyebrow" style="left:75px;top:335px">Welcome To</div>
<div class="abs hero-title" style="left:73px;top:366px">Voltaro Works</div>
<div class="abs hero-desc" style="left:75px;top:420px">production and development company for electronics with emphasis on small series production</div>
<a class="abs btn" href="#" style="left:75px;top:493px;width:136px;height:34px">Read More <span class="arr"><svg width="8" height="8" viewBox="0 0 8 8"><path d="M2.5 1 5.5 4 2.5 7" fill="none" stroke="#0a4b8c" stroke-width="1.5"/></svg></span></a>

<svg class="abs" style="left:0;top:755px" width="1200" height="25" aria-hidden="true">
  <defs><pattern id="teeth" width="80" height="25" patternUnits="userSpaceOnUse"><polygon points="28,0 52,0 60,25 20,25" fill="#fff"/><rect x="0" y="24" width="80" height="1" fill="#fff"/></pattern></defs>
  <rect width="1200" height="25" fill="url(#teeth)"/>
</svg>

<!-- about -->
<div class="abs h2" style="top:851px">About us</div>
<div class="abs rule" style="left:572px;top:906px"></div>

<div class="abs about-frame" style="left:102px;top:936px;width:290px;height:250px"></div>
<div class="abs about-outline" style="left:290px;top:1100px;width:290px;height:245px"></div>
<div class="abs about-photo" style="left:115px;top:949px;width:454px;height:385px" role="img" aria-label="Photo of open industrial switchboard cabinets with breakers and orange wiring"></div>

<div class="abs about-text" style="left:623px;top:941px">
  <p><b>Voltaro Works</b> is a production and development company for<br>electronics with emphasis on small series production. We are today<br>two employees with good and relevant access to additional<br>expertise in the established network. The company was established<br>in 1985 and has since 2001 taken over production equipment and<br>production basis from another company in the same industry.</p>
  <p><b>Norvik Electronics</b>' production department for electronics was<br>decommissioned and sold July 2001. Voltaro Works v/Tor Lunde<br>has taken over production drawings and equipment.</p>
  <p>Our mission is to contribute good and cost effective electronics<br>products for the industrial market,</p>
</div>
<a class="abs btn" href="#" style="left:623px;top:1301px;width:137px;height:33px">Read More <span class="arr"><svg width="8" height="8" viewBox="0 0 8 8"><path d="M2.5 1 5.5 4 2.5 7" fill="none" stroke="#0a4b8c" stroke-width="1.5"/></svg></span></a>

<!-- services -->
<div class="abs services"></div>
<div class="abs h2 light" style="top:1482px">Our Service</div>

<div class="abs svc" style="left:76px">
  <div class="ph" role="img" aria-label="Photo of a row of grey switchboard cabinets in a hall" style="background:linear-gradient(180deg,#e6e8e2,#b8bdb3)"></div>
  <h3>Production</h3>
  <p>Small series production of electronic units in the number of 10 to 200 units.</p>
</div>
<div class="abs svc" style="left:434px">
  <div class="ph" role="img" aria-label="Photo of a warmly lit control room with panel walls" style="background:linear-gradient(180deg,#cfc2a2,#8d7f62)"></div>
  <h3>Devolopment</h3>
  <p>Small series production of electronic units in the number of 10 to 200 units.</p>
</div>
<div class="abs svc" style="left:792px">
  <div class="ph" role="img" aria-label="Photo of an electrician testing a panel with a multimeter" style="background:linear-gradient(120deg,#5b6f8a,#c8a27d 55%,#d9dcdf)"></div>
  <h3>Design</h3>
  <p>Small series production of electronic units in the number of 10 to 200 units.</p>
</div>

<!-- products -->
<div class="abs h2" style="top:2105px">Products</div>

<div class="abs prod" style="left:76px"><div class="shape" role="img" aria-label="Photo of an orange LED beacon light" style="left:35px;top:25px;width:176px;height:225px;border-radius:50% 50% 12px 12px;background:linear-gradient(180deg,#f0a040 0%,#d87a10 55%,#2b2f3f 60%,#1d2030 100%)"></div></div>
<div class="abs prod" style="left:345px"><div class="shape" role="img" aria-label="Photo of an under voltage relay circuit board in a grey enclosure" style="left:67px;top:22px;width:118px;height:236px;border-radius:10px;background:linear-gradient(180deg,#9aa3a0,#2e6a3c 30%,#2a5f36 80%,#8e9694)"></div></div>
<div class="abs prod" style="left:614px"><div class="shape" role="img" aria-label="Photo of a black flame relay module with terminals" style="left:25px;top:32px;width:196px;height:210px;border-radius:4px;background:linear-gradient(180deg,#222 0%,#222 12%,#f4f4f4 13%,#f4f4f4 85%,#222 86%)"></div></div>
<div class="abs prod" style="left:882px"><div class="shape" role="img" aria-label="Photo of a blue panel instrument circuit board" style="left:22px;top:85px;width:205px;height:110px;border-radius:6px;background:linear-gradient(160deg,#2d5ca8,#1a3e80)"></div></div>

<div class="abs prod-name" style="left:68px">LED poducts</div>
<div class="abs prod-name" style="left:341px">Under Voltage<br>Relay</div>
<div class="abs prod-name" style="left:616px">Flame Guard</div>
<div class="abs prod-name" style="left:893px">Panel<br>Instruments</div>

<a class="abs btn" href="#" style="left:531px;top:2586px;width:138px;height:33px;padding-left:29px">View More <span class="arr"><svg width="8" height="8" viewBox="0 0 8 8"><path d="M2.5 1 5.5 4 2.5 7" fill="none" stroke="#0a4b8c" stroke-width="1.5"/></svg></span></a>

<!-- footer band -->
<svg class="abs" style="left:0;top:2875px" width="1200" height="22" aria-hidden="true">
  <defs><pattern id="teethUp" width="80" height="22" patternUnits="userSpaceOnUse"><polygon points="28,0 52,0 60,22 20,22" fill="#0a4b8c"/></pattern></defs>
  <rect width="1200" height="22" fill="url(#teethUp)"/>
</svg>
<div class="abs footer"></div>

<!-- contact -->
<div class="abs contact-card">
  <h2>Get in Touch</h2>
</div>
<div class="abs field" style="left:266px;top:2779px;width:208px;height:42px">Name*</div>
<div class="abs field" style="left:482px;top:2779px;width:206px;height:42px">Phone*</div>
<div class="abs field" style="left:696px;top:2779px;width:207px;height:42px">Email*</div>
<div class="abs field" style="left:266px;top:2830px;width:637px;height:118px">Message</div>
<a class="abs btn center" href="#" style="left:534px;top:2964px;width:136px;height:33px">Send</a>

<!-- footer content -->
<div class="abs brand" style="left:109px;top:3153px;color:#fff;font-size:30px">Voltaro Works</div>

<div class="abs f-head" style="left:427px;top:3084px">QUICK LINKS</div>
<ul class="f-list abs" style="left:427px;top:0">
  <li style="top:3131px;font-weight:600"><span class="chev">&#8250;</span>Home</li>
  <li style="top:3153px"><span class="chev">&#8250;</span>About us</li>
  <li style="top:3176px"><span class="chev">&#8250;</span>Our Services</li>
  <li style="top:3198px"><span class="chev">&#8250;</span>Products</li>
  <li style="top:3220px"><span class="chev">&#8250;</span>Contact us</li>
</ul>

<div class="abs f-head" style="left:632px;top:3084px">CONTACT INFO</div>
<ul class="f-list abs" style="left:632px;top:0">
  <li style="top:3131px"><svg width="12" height="12" viewBox="0 0 24 24" style="margin-right:10px;vertical-align:-1px"><path fill="#fff" d="M6.6 10.8a15 15 0 0 0 6.6 6.6l2.2-2.2c.3-.3.7-.4 1-.2 1.1.4 2.3.6 3.6.6.6 0 1 .4 1 1V20c0 .6-.4 1-1 1A17 17 0 0 1 3 4c0-.6.4-1 1-1h3.5c.6 0 1 .4 1 1 0 1.3.2 2.5.6 3.6.1.3 0 .7-.2 1z"/></svg>555-010-2040</li>
  <li style="top:3176px"><svg width="13" height="10" viewBox="0 0 20 14" style="margin-right:9px"><rect x="1" y="1" width="18" height="12" fill="#fff"/><path d="M1.5 1.5 10 8l8.5-6.5" fill="none" stroke="#0a4b8c" stroke-width="1.6"/></svg>info@voltaroworks.com</li>
  <li style="top:3198px;left:26px">Lysvegen 58, N-4610</li>
  <li style="top:3220px"><svg width="12" height="13" viewBox="0 0 24 24" style="margin-right:10px;vertical-align:-1px"><path fill="#fff" d="M12 2a7 7 0 0 0-7 7c0 5 7 13 7 13s7-8 7-13a7 7 0 0 0-7-7zm0 9.5A2.5 2.5 0 1 1 12 6.5a2.5 2.5 0 0 1 0 5z"/></svg>Kvernes, Norway</li>
</ul>

<div class="abs f-head" style="left:880px;top:3084px">NEWSLETTER</div>
<div class="abs news-input" style="left:882px;top:3131px;width:245px;height:41px">Email address</div>
<a class="abs news-btn" href="#" style="left:882px;top:3188px;width:245px;height:40px">SUBSCRIBE</a>

<div class="abs copy" style="left:69px;top:3333px">Copyright © 2022 Voltaro Works. All Rights Reserved.</div>
<span class="abs social first" style="left:991px;top:3330px"></span>
<span class="abs social" style="left:1025px;top:3330px"></span>
<span class="abs social" style="left:1058px;top:3330px"></span>
<span class="abs social" style="left:1091px;top:3330px"></span>

</body>
</html>
```